Whiskey Glass Packaging Design Project

I require a package design for my products - Whiskey Tasting glasses ( Set of 4) I will be selling on the Brevora USA platform. Must be of high quality, something that the customer will be very impressed with after opening once it arrives at their doorstop. To get an idea of competition please take a look on Brevora.com and do a search on Whiskey Glasses - Scotch Glasses. The competition is very good so we require something that will be better than them. We have a home and kitchen brand that caters to an audience that appreciate fine whiskey / oak barrels / cigars ... I can provide logo and content to be placed on box as well as dine line.

Target Market(s)

Men who love all things about Whiskey / Business / Cigars. Men / Women / Wives / Husbands who are looking to buy gifts for Husband / Partner .

Requirements
Must have
• On one side of the box we would like for the following wording to be included.
The KERAVIND snifter glass is one of the ideal glasses that all enthusiasts will swear by. The glass is a type of stemware, a short - stemmed glass whose vessel has a wide bottom and a relatively narrow top. It is mostly used to serve aged brown Scotch / Whiskey, Bourbon and Brandy.
It's simply a matter of raising the glass to take in a whiff of the aromas before taking a sip. We hope the graceful design of this KERAVIND Whiskey glass adds a nice touch of class to the presentation of your favourite drop ! Enjoy !
Nice to have
• Elegant, soothing and relaxing feel.
Should not have
• Nothing aggressive, racist, homosexual / anti gay .

```html
<!DOCTYPE html>
<html lang="en">
<head>
<meta charset="utf-8">
<title>KERAVIND Snifter Box Dieline 170x170x110mm</title>
<link rel="stylesheet" href="https://fonts.googleapis.com/css2?family=Crimson+Text&family=Montserrat:wght@300;400&family=Source+Sans+3:wght@400;600&display=swap">
<style>
  :root {
    --paper: #ffffff;
    --board: #000000;
    --cut-line: #1aaee6;
    --brand-orange: #e8892a;
    --copy-white: #ffffff;
    --band-dark: #5a3a14;
    --band-light: #c8913a;
  }
  html, body {
    margin: 0;
    padding: 0;
    width: 1200px;
    height: 638px;
    overflow: hidden;
    background: var(--paper);
  }
  .dieline {
    display: block;
    width: 1200px;
    height: 638px;
  }
  .size-label {
    font-family: "Crimson Text", serif;
    font-size: 92px;
    fill: #000;
  }
  .board { fill: var(--board); }
  .cut { fill: none; stroke: var(--cut-line); stroke-width: 3; stroke-linejoin: round; }
  .brand-name {
    font-family: "Montserrat", sans-serif;
    font-weight: 400;
    font-size: 26px;
    letter-spacing: 9px;
    fill: var(--brand-orange);
  }
  .product-title {
    font-family: "Montserrat", sans-serif;
    font-weight: 400;
    font-size: 19px;
    letter-spacing: 4px;
    fill: var(--brand-orange);
  }
  .product-sub {
    font-family: "Montserrat", sans-serif;
    font-weight: 400;
    font-size: 9px;
    letter-spacing: 2.6px;
    fill: var(--copy-white);
  }
  .story-copy {
    font-family: "Source Sans 3", sans-serif;
    font-size: 10.5px;
    fill: var(--copy-white);
  }
  .story-copy .brand-mention { font-weight: 600; }
  .glass-icon { fill: none; stroke: var(--copy-white); stroke-width: 2; }
</style>
</head>
<body>
<svg class="dieline" viewBox="0 0 2560 1361" preserveAspectRatio="none" xmlns="http://www.w3.org/2000/svg">
  <defs>
    <linearGradient id="band-tone" x1="0" y1="0" x2="0" y2="1">
      <stop offset="0" stop-color="var(--band-dark)"/>
      <stop offset="0.5" stop-color="var(--band-light)"/>
      <stop offset="1" stop-color="var(--band-dark)"/>
    </linearGradient>
  </defs>

  <text class="size-label" x="195" y="115">170x170x110mm</text>

  <rect class="board" x="127" y="148" width="2403" height="1175"/>

  <!-- gold lattice bands -->
  <rect class="lattice-band" x="123" y="520" width="2407" height="75" fill="url(#band-tone)" opacity="0.75" role="img" aria-label="Gold diamond lattice band wrapping the box top edge"/>
  <rect class="lattice-band" x="123" y="882" width="2407" height="75" fill="url(#band-tone)" opacity="0.75" role="img" aria-label="Gold diamond lattice band wrapping the box bottom edge"/>

  <!-- cut and crease lines -->
  <g class="cut">
    <!-- glue flap -->
    <polyline points="154,548 67,598 67,877 154,928"/>

    <!-- panel: front -->
    <rect x="154" y="248" width="589" height="978"/>
    <line x1="154" y1="548" x2="743" y2="548"/>
    <line x1="154" y1="928" x2="743" y2="928"/>
    <path d="M189,252 V198 L222,165 H425 L442,182 V200 a7,7 0 0 0 14,0 V182 L472,165 H675 L709,198 V252 Z"/>
    <path d="M189,1222 V1276 L222,1309 H425 L442,1292 V1274 a7,7 0 0 1 14,0 V1292 L472,1309 H675 L709,1276 V1222 Z"/>

    <!-- panel: side one -->
    <path d="M754,257 V200 a30,30 0 0 1 30,-30 H1293 a30,30 0 0 1 30,30 V257 Z"/>
    <rect x="1032" y="213" width="13" height="304" rx="6.5"/>
    <line x1="743" y1="552" x2="1333" y2="552"/>
    <line x1="743" y1="923" x2="1333" y2="923"/>
    <path d="M754,1218 V1275 a30,30 0 0 0 30,30 H1293 a30,30 0 0 0 30,-30 V1218 Z"/>
    <rect x="1032" y="958" width="13" height="304" rx="6.5"/>

    <!-- panel: back -->
    <rect x="1333" y="248" width="589" height="978"/>
    <line x1="1333" y1="548" x2="1922" y2="548"/>
    <line x1="1333" y1="928" x2="1922" y2="928"/>
    <path d="M1368,252 V198 L1401,165 H1604 L1621,182 V200 a7,7 0 0 0 14,0 V182 L1651,165 H1854 L1888,198 V252 Z"/>
    <path d="M1368,1222 V1276 L1401,1309 H1604 L1621,1292 V1274 a7,7 0 0 1 14,0 V1292 L1651,1309 H1854 L1888,1276 V1222 Z"/>

    <!-- panel: side two -->
    <path d="M1933,257 V200 a30,30 0 0 1 30,-30 H2472 a30,30 0 0 1 30,30 V257 Z"/>
    <rect x="2211" y="213" width="13" height="304" rx="6.5"/>
    <polyline points="1922,552 2512,552 2512,923 1922,923"/>
    <path d="M1933,1218 V1275 a30,30 0 0 0 30,30 H2472 a30,30 0 0 0 30,-30 V1218 Z"/>
    <rect x="2211" y="958" width="13" height="304" rx="6.5"/>
  </g>

  <!-- lid: product label -->
  <g class="product-label">
    <rect class="glass-icon" x="330" y="368" width="36" height="50" rx="14" role="img" aria-label="Snifter glass line icon"/>
    <text class="product-title" x="403" y="382">SNIFTER</text>
    <text class="product-sub" x="403" y="400">WHISKEY TASTING GLASSES</text>
    <text class="product-sub" x="403" y="417">(SET OF 4)</text>
  </g>

  <!-- front: brand -->
  <text class="brand-name" x="453" y="790" text-anchor="middle">KERAVIND</text>

  <!-- side one: product label -->
  <g class="product-label">
    <rect class="glass-icon" x="1027" y="688" width="24" height="33" rx="9" role="img" aria-label="Snifter glass line icon"/>
    <text class="product-title" x="1043" y="745" text-anchor="middle">SNIFTER</text>
    <text class="product-sub" x="1042" y="762" text-anchor="middle">WHISKEY TASTING GLASSES</text>
    <text class="product-sub" x="1042" y="779" text-anchor="middle">(SET OF 4)</text>
  </g>

  <!-- back lid: inverted brand -->
  <text class="brand-name" x="1627" y="333" text-anchor="middle" transform="rotate(180 1627 333)">KERAVIND</text>

  <!-- back: brand -->
  <text class="brand-name" x="1632" y="790" text-anchor="middle">KERAVIND</text>

  <!-- side two: brand story -->
  <text class="story-copy" text-anchor="middle">
    <tspan x="2218" y="689">The <tspan class="brand-mention">KERAVIND</tspan> snifter glass is one of the ideal glasses that</tspan>
    <tspan x="2218" y="705">all enthusiasts will swear by. The glass is a type of stemware, a short - stemmed</tspan>
    <tspan x="2218" y="721">glass whose vessel has a wide bottom and a relatively narrow top. It is mostly used</tspan>
    <tspan x="2218" y="737">to serve aged brown Scotch / Whiskey, Bourbon and Brandy.</tspan>
    <tspan x="2218" y="766">It's simply a matter of raising the glass to take in a whiff of the aromas</tspan>
    <tspan x="2218" y="782">before taking a sip. We hope the graceful design of this <tspan class="brand-mention">KERAVIND</tspan> Whiskey glass</tspan>
    <tspan x="2218" y="798">adds a nice touch of class to the presentation of your favourite drop ! Enjoy !</tspan>
  </text>
</svg>
</body>
</html>
```